" Estamos a vinte anos no mercado, porem somos de porte pequeno em relação ao mercado. Fazemos abertura/encerramento de empresas, parte contábil, fiscal e departamento pessoal. Além de assessorar o cliente em duvidas corriqueiras que venham a sugir. "

```html
<!DOCTYPE html>
<html lang="pt-BR">
<head>
<meta charset="UTF-8">
<title>Corvani Assessoria Contábil – Cartão de visita</title>
<link rel="stylesheet" href="https://fonts.googleapis.com/css2?family=Arimo:wght@400;700&display=swap">
<style>
  :root {
    --page-bg: #e9e7e3;
    --navy: #1d3e60;
    --card-white: #ffffff;
    --text-light: #f2f5f8;
    --accent-bar: #8d9db2;
    --tagline: #5a6b80;
    --shadow: rgba(0, 0, 0, 0.28);
  }
  html, body {
    margin: 0;
    padding: 0;
    width: 1200px;
    height: 1200px;
    overflow: hidden;
    background: var(--page-bg);
    font-family: "Arimo", Arial, sans-serif;
  }
  .canvas {
    position: relative;
    width: 1200px;
    height: 1200px;
  }
  .card {
    position: absolute;
    left: 238px;
    width: 890px;
    height: 420px;
    box-shadow: 0 6px 18px var(--shadow);
  }
  .card--back {
    top: 150px;
    background: var(--navy);
  }
  .card--front {
    top: 612px;
    background: var(--card-white);
  }
  .contact {
    position: absolute;
    right: 180px;
    top: 222px;
    margin: 0;
    text-align: right;
    color: var(--text-light);
    font-size: 19px;
    line-height: 24px;
    font-style: normal;
  }
  .contact span { display: block; }
  .accent-bar {
    position: absolute;
    right: 152px;
    top: 222px;
    width: 20px;
    height: 146px;
    background: var(--accent-bar);
    opacity: 0.8;
  }
  .brand {
    position: absolute;
    left: 210px;
    top: 168px;
    display: flex;
    align-items: center;
    gap: 26px;
  }
  .brand-dot {
    width: 54px;
    height: 54px;
    border-radius: 50%;
    background: var(--navy);
  }
  .brand-text { display: flex; flex-direction: column; }
  .brand-name {
    margin: 0;
    font-size: 66px;
    font-weight: 400;
    line-height: 1;
    color: var(--navy);
    letter-spacing: 1px;
  }
  .brand-tagline {
    margin: 6px 0 0 4px;
    font-size: 15px;
    letter-spacing: 1.5px;
    text-transform: uppercase;
    color: var(--tagline);
  }
</style>
</head>
<body>
<main class="canvas">
  <section class="card card--back" aria-label="Verso do cartão">
    <address class="contact">
      <span>Nome Sobrenome</span>
      <span>função</span>
      <span>(00)0000-0000</span>
      <span>contato@exemplo.com</span>
      <span>rua sem nome,00</span>
      <span>bairro sem nome , cidade sem nome</span>
    </address>
    <div class="accent-bar"></div>
  </section>

  <section class="card card--front" aria-label="Frente do cartão">
    <div class="brand">
      <div class="brand-dot"></div>
      <div class="brand-text">
        <h1 class="brand-name">Corvani</h1>
        <p class="brand-tagline">Assessoria Contábil</p>
      </div>
    </div>
  </section>
</main>
</body>
</html>
```